Business Card Design

we specialise in supply of custom uniforms - teamwear to Schools and sporting clubs, see our website: www.harbourkitcove.com.au, our main corporate colour is black and white, with small amount of gold/yellow

Industry/Entity Type

Business

Contact Information for Business Card

Harbour Kit Cove
Travis Okafor
Ph 03 6218 5097
Mobile 0462 318 740
email: travis@harbourkitcove.com.au
www.harbourkitcove.com.au
Like us online

Requirements
Must have
• modern look & feel

```html
<!DOCTYPE html>
<html lang="en">
<head>
<meta charset="utf-8">
<title>Harbour Kit Cove – Business Card</title>
<link href="https://fonts.googleapis.com/css2?family=Lato:wght@400;700;900&display=swap" rel="stylesheet">
<style>
  :root {
    --bg: #2b2b2b;
    --card: #141414;
    --card-light: #1e1e1e;
    --white: #ffffff;
    --text: #e6e6e6;
    --gold: #f7c31b;
  }
  * { margin: 0; padding: 0; box-sizing: border-box; }
  html, body { width: 1200px; height: 1000px; overflow: hidden; }
  body {
    background: var(--bg);
    font-family: "Lato", Arial, sans-serif;
    display: flex; align-items: center; justify-content: center;
  }
  .card {
    position: relative;
    width: 900px; height: 520px;
    border-radius: 22px;
    overflow: hidden;
    background: radial-gradient(circle at 40% 35%, var(--card-light), var(--card) 70%);
    box-shadow: 0 20px 50px rgba(0,0,0,.5);
    color: var(--text);
  }
  .showroom {
    position: absolute; top: 52px; right: 60px;
    text-align: right; font-size: 19px; line-height: 1.3;
  }
  .showroom .label { color: var(--gold); }
  .brand {
    position: absolute; top: 170px; left: 70px;
    display: flex; align-items: center; gap: 18px;
  }
  .brand-mark { width: 70px; height: 70px; border-radius: 50%; background: var(--white); }
  .brand-name {
    font-weight: 900; font-size: 46px; color: var(--white);
    letter-spacing: -0.5px; line-height: 1;
  }
  .contacts {
    position: absolute; top: 270px; right: 60px;
    list-style: none; text-align: right; font-size: 19px; line-height: 1.45;
  }
  .contacts li { display: flex; justify-content: flex-end; align-items: center; gap: 12px; }
  .contacts svg { width: 20px; height: 20px; fill: var(--gold); flex: none; }
  .contacts .no-icon { padding-right: 32px; }
  .person {
    position: absolute; left: 70px; top: 345px;
    font-size: 20px; line-height: 1.3;
  }
  .person .name { font-size: 28px; font-weight: 700; color: var(--white); letter-spacing: .5px; }
  .person .role, .person .social { color: var(--gold); }
  .stripes { position: absolute; left: 0; right: 0; bottom: 0; }
  .stripe-white { height: 7px; background: var(--white); margin-bottom: 10px; }
  .stripe-gold { height: 32px; background: var(--gold); }
</style>
</head>
<body>
  <div class="card">
    <div class="showroom">
      <div class="label">Showroom Visits (by Appointment only)</div>
      <div>7/19 Marlin Ave, Kelpview Tas 7310</div>
      <div>(Anchor House Building)</div>
    </div>

    <div class="brand">
      <span class="brand-mark"></span>
      <span class="brand-name">Harbour Kit Cove</span>
    </div>

    <ul class="contacts">
      <li>03 6218 5097
        <svg viewBox="0 0 24 24"><path d="M6.6 10.8a15 15 0 0 0 6.6 6.6l2.2-2.2a1 1 0 0 1 1-.25 11 11 0 0 0 3.6.6 1 1 0 0 1 1 1V20a1 1 0 0 1-1 1A17 17 0 0 1 3 4a1 1 0 0 1 1-1h3.5a1 1 0 0 1 1 1 11 11 0 0 0 .6 3.6 1 1 0 0 1-.25 1z"/></svg>
      </li>
      <li>0462 318 740
        <svg viewBox="0 0 24 24"><path d="M7 1h10a2 2 0 0 1 2 2v18a2 2 0 0 1-2 2H7a2 2 0 0 1-2-2V3a2 2 0 0 1 2-2zm0 3v14h10V4zm5 15.5a1 1 0 1 0 0 2 1 1 0 0 0 0-2z"/></svg>
      </li>
      <li>travis@harbourkitcove.com.au
        <svg viewBox="0 0 24 24"><path d="M2 5h20v14H2zm2 2v.5l8 5.5 8-5.5V7zm0 3v7h16v-7l-8 5.5z"/></svg>
      </li>
      <li>www.harbourkitcove.com.au
        <svg viewBox="0 0 24 24"><path d="M12 2a10 10 0 1 0 0 20 10 10 0 0 0 0-20zm-1 17.9A8 8 0 0 1 4.1 11H7c.1 3 1.6 6.5 4 8.9zM7 9H4.3A8 8 0 0 1 11 4.1C8.6 6.5 7.2 8 7 9zm2 0c.3-1.8 1.4-3.5 3-5 1.6 1.5 2.7 3.2 3 5zm0 2h6c-.2 2.8-1.3 5.5-3 7.6C10.3 16.5 9.2 13.8 9 11zm4 8.9c2.4-2.4 3.9-5.9 4-8.9h2.9a8 8 0 0 1-6.9 8.9zM17 9c-.2-1-1.6-2.5-4-4.9A8 8 0 0 1 19.7 9z"/></svg>
      </li>
    </ul>

    <div class="person">
      <div class="name">TRAVIS OKAFOR</div>
      <div class="role">Sales</div>
      <div>P.O. Box 318, Kelpview TAS 7310</div>
      <div class="social">Like us online</div>
    </div>

    <div class="stripes">
      <div class="stripe-white"></div>
      <div class="stripe-gold"></div>
    </div>
  </div>
</body>
</html>
```